Cedarline Health Business card

We want a business card that matches our business theme. Our website is www.swiftcarehub.example
The company name is Cedarline Health
The persons having the business cards will be doctors
My logo is attached.
We have a drive-thru medical center where our motto is Fast, Reliable, and Convenient. Our goal is to change the medical space while utilizing technologies, keeping a professional and clean look

Medical

Info on the card should be: Name, Position, Cell number, website, email address, possibly the office line as well

Requirements
Must have
• Logo
Nice to have
• Professional medical feel with our logo colors incorporated

```html
<!DOCTYPE html>
<html lang="en">
<head>
<meta charset="utf-8">
<title>Cedarline Health – Business Card</title>
<link href="https://fonts.googleapis.com/css2?family=Poppins:wght@400;500;600;700&family=Montserrat:wght@500;600;700&display=swap" rel="stylesheet">
<style>
  :root {
    --backdrop: #2a2b2e;
    --card: #ffffff;
    --brand-blue: #1c479d;
    --brand-sky: #3fc3f1;
    --ink: #1d1d1f;
  }
  * { margin: 0; padding: 0; box-sizing: border-box; }
  html, body { width: 1200px; height: 1200px; overflow: hidden; }
  body {
    background: var(--backdrop);
    font-family: "Poppins", sans-serif;
    color: var(--ink);
    position: relative;
  }
  .card {
    position: absolute;
    left: 120px;
    width: 960px;
    height: 548px;
    background: var(--card);
    overflow: hidden;
  }
  .card--back { top: 40px; }
  .card--front { top: 612px; }

  /* Back side */
  .web-band {
    position: absolute;
    left: 170px;
    top: 160px;
    width: 640px;
    height: 130px;
    background: var(--brand-blue);
    border-radius: 0 65px 65px 0;
    display: flex;
    align-items: center;
    padding-left: 160px;
  }
  .web-band__url {
    color: #fff;
    font-family: "Montserrat", sans-serif;
    font-weight: 600;
    font-size: 20px;
    letter-spacing: 3px;
  }

  /* Front side */
  .brand {
    position: absolute;
    left: 50px;
    top: 50px;
    display: flex;
    align-items: center;
    gap: 18px;
  }
  .brand__name {
    font-weight: 700;
    font-size: 46px;
    line-height: 1;
    color: var(--brand-blue);
  }
  .brand__dot {
    width: 56px;
    height: 56px;
    border-radius: 50%;
    background: var(--brand-sky);
  }
  .tagline {
    position: absolute;
    left: 52px;
    top: 130px;
    font-family: "Montserrat", sans-serif;
    font-weight: 500;
    font-size: 22px;
    letter-spacing: 1px;
  }
  .person {
    position: absolute;
    right: 60px;
    top: 190px;
    text-align: right;
  }
  .person__name {
    font-family: "Montserrat", sans-serif;
    font-weight: 700;
    font-size: 32px;
    color: var(--brand-blue);
    letter-spacing: 1px;
  }
  .person__role {
    font-family: "Montserrat", sans-serif;
    font-weight: 600;
    font-size: 22px;
    letter-spacing: 1px;
  }
  .divider {
    position: absolute;
    left: 60px;
    right: 60px;
    top: 318px;
    height: 2px;
    background: var(--brand-blue);
  }
  .contacts {
    position: absolute;
    left: 60px;
    top: 350px;
    list-style: none;
    font-size: 22px;
    line-height: 1.6;
  }
  .contacts li { display: flex; align-items: center; gap: 14px; }
  .contacts svg { width: 26px; height: 26px; flex: none; }
  .address {
    position: absolute;
    right: 60px;
    top: 360px;
    font-style: normal;
    font-size: 22px;
    line-height: 1.5;
    width: 400px;
  }
  .edge-stripe {
    position: absolute;
    left: 0; right: 0; bottom: 0;
    height: 16px;
    background: linear-gradient(90deg, var(--brand-blue) 0 52%, var(--brand-sky) 52% 100%);
  }
</style>
</head>
<body>

<section class="card card--back" aria-label="Card back">
  <div class="web-band">
    <span class="web-band__url">www.SWIFTCAREHUB.example</span>
  </div>
</section>

<section class="card card--front" aria-label="Card front">
  <div class="brand">
    <span class="brand__name">Cedarline Health</span>
    <span class="brand__dot"></span>
  </div>
  <p class="tagline">CARE | CLARITY | COMFORT</p>

  <div class="person">
    <p class="person__name">RENATA VELLORIN</p>
    <p class="person__role">CEO</p>
  </div>

  <div class="divider"></div>

  <ul class="contacts">
    <li>
      <svg viewBox="0 0 26 26" aria-hidden="true"><circle cx="13" cy="13" r="13" fill="#1c479d"/><rect x="8.5" y="7" width="9" height="12" rx="1.5" fill="none" stroke="#fff" stroke-width="1.8"/></svg>
      +1 (555) 014-2290
    </li>
    <li>
      <svg viewBox="0 0 26 26" aria-hidden="true"><circle cx="13" cy="13" r="13" fill="#1c479d"/><rect x="6.5" y="8.5" width="13" height="9" fill="none" stroke="#fff" stroke-width="1.6"/><path d="M6.5 8.5 13 14l6.5-5.5" fill="none" stroke="#fff" stroke-width="1.6"/></svg>
      info@swiftcarehub.example
    </li>
    <li>
      <svg viewBox="0 0 26 26" aria-hidden="true"><circle cx="13" cy="13" r="13" fill="#1c479d"/><circle cx="13" cy="13" r="7" fill="none" stroke="#fff" stroke-width="1.5"/><ellipse cx="13" cy="13" rx="3" ry="7" fill="none" stroke="#fff" stroke-width="1.3"/><path d="M6 13h14" stroke="#fff" stroke-width="1.3"/></svg>
      www.swiftcarehub.example
    </li>
  </ul>

  <address class="address">
    42 Harbour View Road, Eastport<br>
    7 Crescent Lane, Hill Road<br>
    Bayside
  </address>

  <div class="edge-stripe"></div>
</section>

</body>
</html>
```